Business Card

I need a business card that really pops for a potential customer or person who refers a personal injury lead. I want to highlight our office locations, but only address that needs to be on the card is my office's main address. I want a sleek, modern and minimalist design.

```html
<!DOCTYPE html>
<html lang="en">
<head>
<meta charset="utf-8">
<title>Lakeshore Injury Counsel — Business Card</title>
<link rel="stylesheet" href="https://fonts.googleapis.com/css2?family=Inter:wght@400;700&display=swap">
<style>
  :root {
    --backdrop: #dcdddf;
    --card-stock: #efeeeb;
    --ink-dark: #2b2b2b;
    --ink-soft: #7c7c7c;
    --card-edge: #1e1e1e;
  }
  html, body {
    margin: 0;
    padding: 0;
    width: 1200px;
    height: 1051px;
    overflow: hidden;
    background: var(--backdrop);
    font-family: "Inter", Arial, sans-serif;
  }
  .card-set {
    position: absolute;
    inset: 0;
    display: flex;
    align-items: center;
    justify-content: center;
    gap: 40px;
  }
  .card {
    width: 520px;
    height: 297px;
    background: var(--card-stock);
    border-bottom: 4px solid var(--card-edge);
    box-shadow: 0 14px 30px rgba(0,0,0,0.12);
    box-sizing: border-box;
    display: flex;
    flex-direction: column;
    align-items: center;
    justify-content: center;
    text-align: center;
  }
  .card-back .holder-name {
    margin: 0;
    font-weight: 700;
    font-size: 19px;
    color: var(--ink-dark);
    letter-spacing: 0.01em;
  }
  .card-back .holder-title {
    margin: 4px 0 0;
    font-size: 13px;
    color: var(--ink-soft);
  }
  .card-back .divider {
    width: 64px;
    height: 1px;
    background: var(--ink-dark);
    margin: 16px 0 14px;
  }
  .card-back .contact {
    margin: 0;
    font-size: 13px;
    line-height: 1.6;
    color: var(--ink-soft);
  }
  .card-front .firm-name {
    margin: 0;
    font-weight: 400;
    font-size: 24px;
    letter-spacing: 0.22em;
    text-transform: uppercase;
    color: var(--ink-dark);
  }
</style>
</head>
<body>
  <main class="card-set">
    <section class="card card-back" aria-label="Card back with contact details">
      <h1 class="holder-name">HAROLD J. WHITMAN</h1>
      <p class="holder-title">President / CEO</p>
      <div class="divider"></div>
      <p class="contact">
        312-555-0148<br>
        info@lakeshoreinjurycounsel.com<br>
        www.lakeshoreinjurycounsel.com<br>
        210 West Harbor Street, Suite 1800, Chicago, IL 60601
      </p>
    </section>
    <section class="card card-front" aria-label="Card front with firm name">
      <p class="firm-name">Lakeshore Injury Counsel</p>
    </section>
  </main>
</body>
</html>
```